TM Homes - Stone Kraft Design

Looking for a double sides design, 1 side for my realestate and the other for home building. ( TM Homes on 1 side, Stone Kraft card on the other Side
Side 1 - Rivka Dorn ~ Vex Homes logo and Company ( the Property quarter )
Rivka Dorn
Rivka@Rivkadorn.example
IG - Rivka_Pmq_Agent
FB - rivkad
Cell - 5550193746
3847 17 St Nw

Side 2
Rivka Dorn
5550193746
IG - Stonekraft_Pmq
Stonekraftdev@mailbox.example

Target Market(s)

Home buyers/ sellers

Industry/Entity Type

Home builders - Realestate

Contact Information for Business Card

Above

Requirements
Must have
• Black OR White background - my information -

```html
<!DOCTYPE html>
<html lang="en">
<head>
<meta charset="utf-8">
<title>Stone Kraft Developments and Rivka Dorn business cards</title>
<link rel="stylesheet" href="https://fonts.googleapis.com/css2?family=Libre+Baskerville:wght@400;700&display=swap">
<style>
  :root {
    --backdrop: #242424;
    --card: #222126;
    --red: #d1213a;
    --white: #ffffff;
    --muted: #e9e9ec;
    --serif: "Libre Baskerville", "Times New Roman", serif;
  }
  * { box-sizing: border-box; margin: 0; padding: 0; }
  html, body {
    width: 1200px; height: 780px; overflow: hidden;
    background: var(--backdrop);
    font-family: var(--serif);
  }
  .canvas { position: relative; width: 1200px; height: 780px; }

  .card {
    position: absolute;
    width: 540px; height: 310px;
    background: var(--card);
    border-bottom: 6px solid var(--red);
    border-left: 3px solid var(--red);
    box-shadow: 0 14px 30px rgba(0,0,0,.55);
    overflow: hidden;
  }
  .card--builder { left: 40px; top: 90px; }
  .card--realty  { left: 620px; top: 380px; }

  .brand {
    position: absolute;
    display: flex; align-items: center; gap: 10px;
    color: var(--white);
    font-family: var(--serif);
    font-weight: 400;
    letter-spacing: 1px;
  }
  .brand__mark { width: 12px; height: 12px; background: var(--red); }
  .card--builder .brand { left: 44px; top: 58px; font-size: 24px; text-transform: uppercase; }
  .card--realty .brand--personal { left: 44px; top: 40px; font-size: 26px; text-transform: uppercase; }
  .card--realty .brand--office { right: 34px; top: 34px; font-size: 19px; }

  .name {
    position: absolute;
    left: 0;
    display: flex; align-items: center;
    font-weight: 700;
    font-size: 30px;
    color: var(--white);
  }
  .name__tab { width: 24px; height: 34px; background: var(--red); margin-right: 16px; }
  .name__last { color: var(--red); margin-left: 10px; }
  .card--builder .name { top: 150px; }
  .card--realty .name { top: 110px; }

  .address {
    position: absolute; left: 42px; top: 160px;
    font-size: 14px; color: var(--muted);
  }

  .contacts {
    position: absolute; left: 42px;
    list-style: none;
    font-size: 13px; color: var(--muted);
  }
  .card--builder .contacts { top: 208px; }
  .card--realty .contacts { top: 188px; }
  .contacts li { display: flex; align-items: center; gap: 10px; height: 20px; }
  .contacts svg { width: 13px; height: 13px; flex: none; fill: var(--white); }
  .dot { width: 11px; height: 11px; border-radius: 50%; background: var(--white); flex: none; margin: 0 1px; }
</style>
</head>
<body>
<main class="canvas">

  <section class="card card--builder" aria-label="Stone Kraft Developments card">
    <div class="brand"><span class="brand__mark"></span>Stone Kraft Developments</div>
    <h1 class="name"><span class="name__tab"></span>Rivka<span class="name__last">Dorn</span></h1>
    <ul class="contacts">
      <li><svg viewBox="0 0 24 24"><path d="M6.6 10.8a15.1 15.1 0 0 0 6.6 6.6l2.2-2.2c.3-.3.7-.4 1-.2 1.1.4 2.3.6 3.6.6.6 0 1 .4 1 1V20c0 .6-.4 1-1 1A17 17 0 0 1 3 4c0-.6.4-1 1-1h3.5c.6 0 1 .4 1 1 0 1.3.2 2.5.6 3.6.1.3 0 .7-.2 1z"/></svg>5550193746</li>
      <li><span class="dot"></span>Stonekraft_Pmq</li>
      <li><svg viewBox="0 0 24 24"><path d="M2 5h20v14H2zm2 2v.5l8 5 8-5V7zm0 3v7h16v-7l-8 5z"/></svg>Stonekraftdev@mailbox.example</li>
    </ul>
  </section>

  <section class="card card--realty" aria-label="Rivka Dorn realty card">
    <div class="brand brand--personal"><span class="brand__mark"></span>Rivka Dorn</div>
    <div class="brand brand--office">the Property quarter</div>
    <h2 class="name"><span class="name__tab"></span>Rivka<span class="name__last">Dorn</span></h2>
    <p class="address">3847 17 St Nw</p>
    <ul class="contacts">
      <li><svg viewBox="0 0 24 24"><path d="M6.6 10.8a15.1 15.1 0 0 0 6.6 6.6l2.2-2.2c.3-.3.7-.4 1-.2 1.1.4 2.3.6 3.6.6.6 0 1 .4 1 1V20c0 .6-.4 1-1 1A17 17 0 0 1 3 4c0-.6.4-1 1-1h3.5c.6 0 1 .4 1 1 0 1.3.2 2.5.6 3.6.1.3 0 .7-.2 1z"/></svg>5550193746</li>
      <li><span class="dot"></span>rivkad</li>
      <li><span class="dot"></span>Rivka_Pmq_Agent</li>
      <li><svg viewBox="0 0 24 24"><path d="M2 5h20v14H2zm2 2v.5l8 5 8-5V7zm0 3v7h16v-7l-8 5z"/></svg>Rivka@Rivkadorn.example</li>
      <li><svg viewBox="0 0 24 24"><path d="M12 2a10 10 0 1 0 0 20 10 10 0 0 0 0-20zm0 2c.9 0 2.1 1.7 2.6 5H9.4C9.9 5.7 11.1 4 12 4zM4.3 11h3c0-.7.1-1.4.2-2H5a8 8 0 0 0-.7 2zm0 2a8 8 0 0 0 .7 2h2.5l-.2-2zm5 0 .1 2h5.2l.1-2zm0-2h5.4l-.1-2H9.4zm7.4 0h3a8 8 0 0 0-.7-2h-2.5zm0 2-.2 2H19a8 8 0 0 0 .7-2zM12 20c-.9 0-2.1-1.7-2.6-5h5.2c-.5 3.3-1.7 5-2.6 5z"/></svg>www.rivkadorn.example</li>
    </ul>
  </section>

</main>
</body>
</html>
```